New Website for novelty yarn producer

We need a new website for our company, Tarvek. We make highly tailored yarns for weavers worldwide. This year marks our 40th anniversary and we want to evolve our image and identity.

Our temporary website can be found at:
www.tarvekyarns.com

Our only concern in that throughout the website the protagonist must be our client, we make their creations possible and are highly adaptable both during the ideation process of the yarn as well as in the production. This is at the core of the way we do business and is summarised within the concept of FPM (Fluid Partner Method).

Industry/Entity Type

Textile

Number of Pages Required

1 page

Colors
9bcb3c

Requirements
Must have
• Fluid Partner Method (FPM) - can be found on or current website www.tarvekyarns.com

```html
<!DOCTYPE html>
<html lang="en">
<head>
<meta charset="utf-8">
<title>Tarvek Novelty Yarn Solutions</title>
<link href="https://fonts.googleapis.com/css2?family=Abril+Fatface&family=Roboto:ital,wght@0,300;0,400;0,500;0,700;0,900;1,300&display=swap" rel="stylesheet">
<style>
:root{
  --brand:#9bcb3c;
  --brand-dark:#6fa01f;
  --brand-yellow:#cfdc3e;
  --brand-deep:#6bb03a;
  --ink:#1d1d1d;
  --paper:#ffffff;
  --mist:#e4e4e4;
  --slate:#6a6a6a;
  --footer:#3b3b3b;
  --muted:#cfcfcf;
}
*{box-sizing:border-box;margin:0;padding:0}
html,body{width:1200px;height:2270px;overflow:hidden}
body{font-family:"Roboto",Arial,sans-serif;color:var(--ink);background:var(--paper);position:relative}
.page{position:relative;width:1200px;height:2270px;overflow:hidden}

/* header */
.site-header{position:absolute;top:0;left:0;width:1200px;height:75px;background:var(--paper)}
.brand-name{position:absolute;left:130px;top:14px;font-family:"Roboto",Arial,sans-serif;font-weight:500;font-size:36px;color:var(--ink);letter-spacing:1px}
.main-nav{position:absolute;right:130px;top:24px;display:flex;gap:29px;font-size:20px;font-weight:300}
.main-nav a{color:var(--ink);text-decoration:none}
.main-nav a.is-current{border-bottom:1px solid var(--brand)}

/* hero */
.hero{position:absolute;top:75px;left:0;width:1200px;height:605px}
.hero-art{position:absolute;inset:0}
.hero-art svg{display:block}
.hero-year{position:absolute;left:290px;top:90px;font-family:"Abril Fatface",Georgia,serif;font-size:460px;line-height:1;color:rgba(255,255,255,.22);letter-spacing:-10px}
.hero-line{position:absolute;font-family:"Abril Fatface",Georgia,serif;font-size:62px;line-height:1}
.hero-line.l1{left:222px;top:170px;color:var(--paper)}
.hero-line.l2{left:480px;top:243px;color:var(--ink)}
.hero-line.l3{left:724px;top:313px;color:var(--paper)}
.rule{position:absolute;height:3px}
.rule.white{background:var(--paper)}
.rule.black{background:var(--ink)}

/* values */
.values{position:absolute;top:680px;left:0;width:1200px;height:400px}
.values svg{position:absolute;inset:0}
.value{position:absolute;top:45px;width:240px;text-align:center;font-size:17px;font-weight:300;line-height:24px;color:#333}
.value.experience{left:180px}
.value.creativity{left:472px}
.value.professionalism{left:764px}
.tag{display:inline-block;position:relative;margin-bottom:14px;padding:4px 28px;color:var(--paper);font-weight:500;font-size:22px}
.tag::before{content:"";position:absolute;inset:0;background:linear-gradient(90deg,var(--brand-dark),var(--brand));transform:skewX(-22deg);z-index:-1}
.tag span{position:relative}
.value em{font-style:italic}

/* about */
.about{position:absolute;top:1080px;left:0;width:1200px;height:526px;background:var(--brand)}
.about-photo{position:absolute;inset:0}
.about-copy{position:absolute;left:150px;top:50px;width:590px;text-align:center;color:var(--paper);font-size:17px;line-height:24px}
.about-copy h2{font-weight:700;font-size:48px;line-height:1;margin-bottom:28px}
.about-copy p{margin-bottom:24px}
.btn{display:inline-block;position:relative;padding:8px 30px;color:var(--paper);font-size:17px;font-weight:500;text-transform:uppercase;text-decoration:none}
.btn::before{content:"";position:absolute;inset:0;background:linear-gradient(180deg,var(--brand),var(--brand-dark));transform:skewX(-18deg);border:1px solid #5f8c1a}
.btn span{position:relative}
.numbers{position:absolute;left:780px;top:60px;width:400px;color:var(--paper)}
.numbers h3{margin-left:65px;font-size:35px;font-weight:700;margin-bottom:22px}
.stat{position:absolute;display:flex;align-items:center;gap:14px}
.stat b{font-size:58px;font-weight:700;line-height:1}
.stat small{font-size:15px;line-height:16px;text-transform:uppercase;font-weight:400}
.stat.years{left:60px;top:105px}
.stat.volume{left:20px;top:205px}
.stat.brands{left:-20px;top:300px}

/* method */
.method{position:absolute;top:1606px;left:0;width:1200px;height:452px;background:linear-gradient(180deg,#727272,var(--slate))}
.method-mark{position:absolute;left:132px;top:148px;width:170px;height:170px;border-radius:50%;border:4px solid var(--brand)}
.method-divider{position:absolute;left:330px;top:148px;width:3px;height:160px;background:var(--paper)}
.method-name{position:absolute;left:363px;top:168px;color:var(--paper);font-weight:300;font-size:34px;line-height:41px;text-transform:uppercase}
.method-copy{position:absolute;left:610px;top:142px;width:400px;color:var(--paper)}
.method-copy h2{font-size:23px;font-weight:700;margin-bottom:14px;text-transform:uppercase}
.method-copy p{font-size:17px;line-height:22px;font-weight:300;margin-bottom:30px}
.method-copy .btn{padding:9px 56px}

/* footer */
.site-footer{position:absolute;top:2058px;left:0;width:1200px;height:212px;background:var(--footer);color:var(--muted)}
.footer-company{position:absolute;left:128px;top:30px;font-size:20px;font-weight:300;color:#eee}
.footer-legal{position:absolute;left:128px;top:64px;font-size:15px;line-height:19px;font-weight:300}
.footer-legal strong{font-weight:500}
.footer-nav{position:absolute;left:810px;top:22px;display:flex;flex-direction:column;font-size:23px;line-height:29px;font-weight:300}
.footer-nav a{color:#eee;text-decoration:none}
.copyright{position:absolute;left:0;width:1200px;top:188px;text-align:center;font-size:10px;letter-spacing:.5px;color:#aaa}
</style>
</head>
<body>
<div class="page">

  <header class="site-header">
    <div class="brand-name">Tarvek</div>
    <nav class="main-nav">
      <a href="#" class="is-current">Home</a>
      <a href="#">About Us</a>
      <a href="#">Fluid Partner Method</a>
      <a href="#">Contact</a>
    </nav>
  </header>

  <section class="hero">
    <div class="hero-art" role="img" aria-label="Close-up photograph of green yarn spools with a diagonal yellow band">
      <svg width="1200" height="605" viewBox="0 0 1200 605">
        <defs>
          <linearGradient id="heroRight" x1="0" y1="0" x2="1" y2="1">
            <stop offset="0" stop-color="#7cc04a"/>
            <stop offset="1" stop-color="#5ea83a"/>
          </linearGradient>
        </defs>
        <rect width="1200" height="605" fill="#9bcb3c"/>
        <polygon points="715,0 1200,0 1200,605 120,605" fill="#cfdc3e"/>
        <polygon points="1045,0 1200,0 1200,605 450,605" fill="url(#heroRight)"/>
      </svg>
    </div>
    <div class="hero-year">40</div>
    <div class="hero-line l1">Tailored</div>
    <div class="rule white" style="left:222px;top:235px;width:262px"></div>
    <div class="hero-line l2">weaving</div>
    <div class="rule white" style="left:222px;top:308px;width:190px"></div>
    <div class="rule black" style="left:412px;top:308px;width:328px"></div>
    <div class="hero-line l3">solutions</div>
    <div class="rule white" style="left:222px;top:378px;width:118px"></div>
    <div class="rule black" style="left:340px;top:378px;width:330px"></div>
    <div class="rule white" style="left:670px;top:378px;width:328px"></div>
  </section>

  <section class="values">
    <svg width="1200" height="400" viewBox="0 0 1200 400" aria-hidden="true">
      <defs>
        <linearGradient id="valuesBg" x1="0" y1="0" x2="1" y2="0">
          <stop offset="0" stop-color="#f4f4f4"/>
          <stop offset=".5" stop-color="#e2e2e2"/>
          <stop offset="1" stop-color="#d8d8d8"/>
        </linearGradient>
      </defs>
      <rect width="1200" height="400" fill="#f6f6f6"/>
      <polygon points="250,0 1200,0 1200,0 1020,400 0,400 0,380" fill="url(#valuesBg)"/>
    </svg>
    <div class="value experience">
      <div class="tag"><span>Experience</span></div>
      <p>Over the years the company has gained the knowledge and skills that define the superiority of our product and the rigor of our work ethic</p>
    </div>
    <div class="value creativity">
      <div class="tag"><span>Creativity</span></div>
      <p>Our belief is that the key to our clients' success is a combination of <em>innovation, creativity</em> and <em>quality</em>. We strive to adapt and re-imagine our product, implementing these principles in order to meet and exceed our clients' demands (every time)</p>
    </div>
    <div class="value professionalism">
      <div class="tag"><span>Professionality</span></div>
      <p>We are a family business at the core. Our company is run with the same values as the Verani family: <em>respect, determination and commitment.</em></p>
    </div>
  </section>

  <section class="about">
    <div class="about-photo" role="img" aria-label="Blurred photograph of a laptop on a wooden desk">
      <svg width="1200" height="526" viewBox="0 0 1200 526">
        <defs>
          <linearGradient id="desk" x1="0" y1="0" x2="0" y2="1">
            <stop offset="0" stop-color="#2c2f22"/>
            <stop offset=".55" stop-color="#4a4a30"/>
            <stop offset="1" stop-color="#2a2418"/>
          </linearGradient>
        </defs>
        <polygon points="0,0 840,0 600,526 0,526" fill="url(#desk)"/>
      </svg>
    </div>
    <div class="about-copy">
      <h2>ABOUT US</h2>
      <p>Our team has decades of experience in providing yarn solutions to weavers around the world, assisting them in the creation of outstanding textiles.</p>
      <p>Our clients can expect open lines of communication, clarity and professionality</p>
      <p>Our focus is our client.</p>
      <p>The success of a client is our success.</p>
      <a href="#" class="btn"><span>Our Heritage</span></a>
    </div>
    <div class="numbers">
      <h3>TYS in Numbers</h3>
      <div class="stat years"><b>40</b><small>Years in<br>business</small></div>
      <div class="stat volume"><b>2</b><small>Million<br>kilograms / yr</small></div>
      <div class="stat brands"><b>8</b><small>Brands</small></div>
    </div>
  </section>

  <section class="method">
    <div class="method-mark"></div>
    <div class="method-divider"></div>
    <div class="method-name">Fluid<br>Partner<br>Method</div>
    <div class="method-copy">
      <h2>Production built around you</h2>
      <p>Versatility and flexibility both in development and production are key in delivering a custom solution capable of giving life to your products.</p>
      <a href="#" class="btn"><span>More</span></a>
    </div>
  </section>

  <footer class="site-footer">
    <div class="footer-company">Tarvek Novelty Yarn Solutions</div>
    <div class="footer-legal">
      <strong>Corvel s.r.l</strong><br>
      Via dei Tessitori 12 - 50140 Lanoro - Italy - Tel. 0555 102040 - Fax 0555 102041<br>
      R.E.A LN 481205 - Reg. Imp. LN 04718230561<br>
      <strong>P. IVA 00482710365</strong> - Cod. Fisc. 04718230561<br>
      Capitale sociale € 91. 541, 99 int. ver.
    </div>
    <nav class="footer-nav">
      <a href="#">Blog</a>
      <a href="#">Team</a>
      <a href="#">Heritage</a>
      <a href="#">Fluid Partner Method</a>
      <a href="#">Contact</a>
    </nav>
    <div class="copyright">© COPYRIGHT 2017. ALL RIGHTS RESERVED.</div>
  </footer>

</div>
</body>
</html>
```